BRIGHTDESK - Remote Tech Support Site

We are looking for a new very responsive and simple website for our brand Brightdesk.com - a remote technical support company.

This company supports customers Globally in different countries throughout Eur/ North America / South America / Asia etc (please keep this in mind and integrate into the idea).

Its important to us that the design is very explanatory, the customer should easily be able to figure out that we provide computer support right away ... I like one page responsive type designs as well without a bunch of menu items

Here are some similar sites we like - but still looking for a unique design that fits out brand "brightdesk" - I have upload also some layouts i like (but the designs are not important just the layouts), youll see it includes consumer business etc which is important.

VOLM.COM - I love how clean it is - nice and white easy to see everything

PLUMWIRE247.COM - also nice the layout and responsive one page design makes it easy to use

corvalfix.com - similar to plumwire design as well - you can get the idea im looking for between the two

You will notice those examples are much different then the attachments I added - again this is more of an idea for possible layouts .. attached is also the logo - could inspire color scheme / blue white black etc

Target Market(s)

Home consumers without computer knowledge , older age 45-65, small medium business ... computer repair - slow computers

Industry/Entity Type

Computer Repair

Logo Text

Brightdesk

Coding

Coded - Design and coding required

Number of Pages Required

1 page

Font styles to use
Sans Serif
Other font styles liked:
• your choice responsive

Colors

Designer to choose colors to be used in the design.

Requirements
Must have
• Clean - responsive - professional design - the name says it all - brightdesk
• CALL TO ACTIONS FOR "Get Help Now!" / "Learn More" etc
Nice to have
• We are looking for a new very responsive and simple website for our brand Brightdesk.com - a remote technical support company.
• This company supports customers Globally in different countries throughout Eur/ North America / South America / Asia etc (please keep this in mind and integrate into the idea).
• Its important to us that the design is very explanatory, the customer should easily be able to figure out that we provide computer support right away ... I like one page responsive type designs as well without a bunch of menu items
• Here are some similar sites we like - but still looking for a unique design that fits out brand "brightdesk" - I have upload also some layouts i like (but the designs are not important just the layouts), youll see it includes consumer business etc which is important.
• VOLM.COM - I love how clean it is - nice and white easy to see everything
• PLUMWIRE247.COM - also nice the layout and responsive one page design makes it easy to use
• corvalfix.com - similar to plumwire design as well - you can get the idea im looking for between the two
Should not have
• dark, packed page - bad small font -

```html
<!DOCTYPE html>
<html lang="en">
<head>
<meta charset="utf-8">
<title>Brightdesk – Remote Tech Support</title>
<link rel="stylesheet" href="https://fonts.googleapis.com/css2?family=Open+Sans:wght@400;600;700;800&display=swap">
<style>
:root{
  --blue:#1f86e6;
  --blue-dark:#0f6cc4;
  --black:#0b0b0b;
  --band-gray:#2f2f31;
  --text:#222;
  --muted:#555;
  --light:#f1f3f6;
  --ring:#e3e5e8;
  --green:#1f9a2d;
  --orange:#f5821f;
  --white:#fff;
}
*{box-sizing:border-box;margin:0;padding:0}
html,body{width:1200px;height:4157px;overflow:hidden}
body{font-family:"Open Sans",Arial,sans-serif;color:var(--text);background:var(--white);position:relative}
section,header,footer{position:absolute;left:0;width:1200px}
.emblem{position:absolute;left:570px;width:60px;height:60px;border-radius:50%;background:var(--blue);border:4px solid #dbe9f8}
.section-title{position:absolute;left:0;width:1200px;text-align:center;color:var(--blue);font-weight:800;font-size:36px;line-height:44px;text-transform:uppercase;letter-spacing:.5px}
.section-lead{position:absolute;left:250px;width:700px;text-align:center;font-size:17px;line-height:24px;color:var(--text)}

/* header */
.site-header{top:0;height:97px;background:linear-gradient(#1a1a1a,#000)}
.brand{position:absolute;left:170px;top:26px;display:flex;align-items:center;gap:10px;color:var(--white);font-weight:700;font-size:30px}
.brand-dot{width:40px;height:40px;border-radius:50%;background:var(--blue)}
.locale{position:absolute;right:95px;top:8px;color:var(--blue);font-size:15px;font-weight:600}
.main-nav{position:absolute;right:95px;top:46px;display:flex;gap:30px;font-size:17px;color:#ddd}
.main-nav .active{color:var(--blue)}

/* hero */
.hero{top:97px;height:457px}
.hero-photo{position:absolute;inset:0;background:linear-gradient(100deg,#5d86c9 0%,#9fb7de 35%,#e9edf2 55%,#bfc3c8 80%,#8d9297 100%)}
.hero-arrow{position:absolute;top:198px;width:42px;height:52px;background:rgba(0,0,0,.55)}
.hero-arrow.left{left:0}.hero-arrow.right{right:0}
.contact-pill{position:absolute;right:0;top:16px;width:160px;height:40px;background:#111;color:var(--white);border-radius:8px 0 0 8px;font-size:16px;line-height:40px;padding-left:20px;letter-spacing:1px}

/* welcome */
.welcome{top:554px;height:214px}
.welcome .section-title{font-size:30px;font-weight:400;text-transform:none}
.welcome .section-title b{font-weight:800}

/* service band */
.service-band{top:768px;height:196px;display:flex}
.service{position:relative;width:400px;height:196px;background:var(--band-gray);color:var(--white);padding:18px 0 0 45px}
.service.feature{background:var(--blue-dark)}
.service h3{font-size:26px;font-weight:400;line-height:30px}
.service h3 b{font-weight:700;display:block}
.service p{font-size:14px;line-height:19px;width:190px;margin-top:16px}
.service svg{position:absolute;right:90px;top:70px}

/* pricing */
.pricing{top:964px;height:505px;background:var(--light)}
.plan{position:absolute;top:211px;width:247px;height:266px;background:var(--white);box-shadow:0 2px 6px rgba(0,0,0,.25);border:6px solid var(--white)}
.plan-head{height:100px;color:var(--white);text-align:center;padding-top:8px}
.plan-head h4{font-size:24px;font-weight:800}
.plan-head .price{font-size:21px;font-weight:800}
.plan-head .price small{font-size:12px}
.plan-head .setup{font-size:15px;font-weight:700}
.plan.green .plan-head{background:var(--green)}
.plan.blue .plan-head{background:var(--blue)}
.plan.orange .plan-head{background:var(--orange)}
.plan ul{list-style:none;text-align:center;font-size:12px;line-height:17px;padding:22px 10px 0}
.plan ul li{margin-bottom:8px}
.plan .more{position:absolute;bottom:0;left:65px;width:105px;text-align:center;font-size:10px;letter-spacing:1px;color:#666;border-bottom:4px solid var(--blue);padding-bottom:2px}
.plan.green .more{border-color:var(--green)}
.plan.orange .more{border-color:var(--orange)}

/* why join */
.why-join{top:1469px;height:659px;background:var(--black)}
.why-item{position:absolute;width:380px;color:var(--white)}
.why-item h4{color:var(--blue);font-size:21px;font-weight:600;margin-bottom:8px}
.why-item p{font-size:17px;line-height:26px}
.devices{position:absolute;left:263px;top:415px;width:693px;height:236px;background:linear-gradient(90deg,#6c6f75,#c9c2d8 45%,#e0d2ea 55%,#6e7279);border-radius:6px}

/* features */
.features{top:2128px;height:809px}
.feature-item{position:absolute;width:190px;text-align:center}
.feature-item svg{display:block;margin:0 auto}
.feature-item h5{color:var(--blue);font-size:19px;font-weight:700;margin-top:12px}
.feature-item p{font-size:14px;line-height:20px;color:#333}

/* consultation */
.consult{top:2937px;height:568px;background:linear-gradient(#fff,#f3f4f6)}
.skyline{position:absolute;left:0;bottom:0;width:1200px;height:230px;background:linear-gradient(transparent,#c8cacd 60%,#9a9da1)}
.video{position:absolute;left:341px;top:208px;width:518px;height:360px;background:#111;border:14px solid #222;border-bottom:none;border-radius:10px 10px 0 0}
.video-inner{position:absolute;inset:0;background:linear-gradient(#2a2c30,#121316)}
.video svg{position:absolute;left:202px;top:125px}

/* request */
.request{top:3505px;height:305px}
.request h2{position:absolute;top:40px;left:0;width:1200px;text-align:center;font-size:36px;font-weight:800;color:#111}
.field{position:absolute;width:291px;height:50px;border:2px solid #cfcfcf;font-size:13px;color:#444;padding:14px 12px}
.btn{position:absolute;background:var(--orange);color:var(--white);font-weight:700;text-align:center}
.btn.help{left:529px;top:250px;width:158px;height:47px;line-height:47px;font-size:16px}

/* footer */
.site-footer{top:3810px;height:347px;background:var(--black);border-top:5px solid var(--blue);color:var(--white)}
.foot-brand{position:absolute;left:172px;top:40px;display:flex;align-items:center;gap:8px;font-size:22px;font-weight:600}
.foot-brand span{width:26px;height:26px;border-radius:50%;background:var(--white)}
.foot-about{position:absolute;left:172px;top:88px;width:285px;font-size:15px;line-height:25px;text-align:justify}
.follow{position:absolute;left:172px;top:224px;font-size:16px;font-weight:700;display:flex;align-items:center;gap:8px}
.follow i{width:28px;height:28px;border:2px solid var(--white);border-radius:50%}
.call{position:absolute;left:172px;top:258px;color:var(--blue);font-weight:700;font-size:19px}
.foot-col h6{font-size:24px;font-weight:700;letter-spacing:1px}
.plans-col{position:absolute;left:485px;top:48px}
.plans-col li{list-style:none;font-size:17px;line-height:33px}
.mail{position:absolute;left:470px;top:262px;color:var(--blue);font-size:16px;font-weight:600}
.news-col{position:absolute;left:684px;top:48px;width:360px}
.news-col p{font-size:16px;line-height:25px;margin-top:12px}
.email-input{position:absolute;left:684px;top:158px;width:231px;height:38px;background:var(--white);border-radius:6px;color:#888;font-size:14px;padding:9px 14px}
.btn.signup{left:931px;top:158px;width:94px;height:38px;line-height:38px;border-radius:6px;font-size:16px}
.badge{position:absolute;top:222px;height:66px;background:#d9d9d9}
.copyright{position:absolute;left:0;bottom:0;width:1200px;height:37px;background:#1b1b1b;text-align:center;font-size:11px;line-height:37px;color:#bbb}
</style>
</head>
<body>

<header class="site-header">
  <div class="brand"><span class="brand-dot"></span>brightdesk</div>
  <div class="locale">United States - EN &nbsp;|&nbsp; Login</div>
  <nav class="main-nav"><span class="active">Home</span><span>About Us</span><span>Services</span><span>Contact Us</span><span>Faqs</span></nav>
</header>

<section class="hero">
  <div class="hero-photo" role="img" aria-label="Support technicians working at computers with headsets"></div>
  <div class="hero-arrow left"><svg width="42" height="52"><path d="M25 18l-8 8 8 8" stroke="#fff" stroke-width="3" fill="none"/></svg></div>
  <div class="hero-arrow right"><svg width="42" height="52"><path d="M17 18l8 8-8 8" stroke="#fff" stroke-width="3" fill="none"/></svg></div>
  <div class="contact-pill">Contact Us</div>
</section>

<section class="welcome">
  <div class="emblem" style="top:14px"></div>
  <h1 class="section-title" style="top:84px">Welcome to <b>BRIGHTDESK</b></h1>
  <p class="section-lead" style="top:128px;left:170px;width:860px">We are a group of technicians who work round the clock to ensure that your PC works perfectly. Get your computer free of suspicious software and have a healthy system</p>
</section>

<section class="service-band">
  <div class="service">
    <h3>FREE<b>Diagnostic</b></h3>
    <p>Get a diagnostic, FOR FREE! Get a free consultation with our staff</p>
    <svg width="50" height="50" viewBox="0 0 50 50" fill="none" stroke="#fff" stroke-width="3"><path d="M5 25v18h40V25"/><path d="M25 5v22M17 19l8 8 8-8"/></svg>
  </div>
  <div class="service feature">
    <h3>Backup your<b>information!</b></h3>
    <p>Saving your files is now EASY! You will be able to retain your personal files without any loss of data</p>
    <svg width="56" height="50" viewBox="0 0 56 50" fill="none" stroke="#fff" stroke-width="3"><path d="M14 38H10a9 9 0 010-18 14 14 0 0127-4 10 10 0 019 22h-4"/><path d="M28 24v22M21 31l7-7 7 7"/></svg>
  </div>
  <div class="service">
    <h3>Get<b>Fixed</b></h3>
    <p>Get fixed, IMMEDIATELY! Our staff will solve your computer issues right before your eyes</p>
    <svg width="50" height="54" viewBox="0 0 50 54" fill="none" stroke="var(--blue)" stroke-width="4"><path d="M25 4l18 7v16c0 12-8 19-18 23C15 46 7 39 7 27V11z"/></svg>
  </div>
</section>

<section class="pricing">
  <div class="emblem" style="top:12px"></div>
  <h2 class="section-title" style="top:82px">Membership Pricing and Plans</h2>
  <p class="section-lead" style="top:130px">Lorem Ipsum is simply dummy text of the printing and typesetting industry. Lorem Ipsum has been the industry's standard dummy text ever since the 1500s</p>

  <div class="plan green" style="left:216px">
    <div class="plan-head"><h4>PREMIUM</h4><div class="price">$19.99 <small>/MONTHLY</small></div><div class="setup">($249-$300 setup fee)</div></div>
    <ul><li>Regular 90-Day Optimization</li><li><b>Unlimited 24/7 Tier 3 Technician Support</b></li></ul>
    <div class="more">LEARN MORE</div>
  </div>
  <div class="plan blue" style="left:493px">
    <div class="plan-head"><h4>PREMIUM PLUS</h4><div class="price">$29.99 <small>/MONTHLY</small></div><div class="setup">($249-$300 setup fee)</div></div>
    <ul><li>Regular 90-Day Optimization</li><li><b>Unlimited 24/7 Tier 3 Technician Support</b></li></ul>
    <div class="more">LEARN MORE</div>
  </div>
  <div class="plan orange" style="left:768px">
    <div class="plan-head"><h4>PLATINUM</h4><div class="price">$39.99 <small>/MONTHLY</small></div><div class="setup">($249-$300 setup fee)</div></div>
    <ul><li>Regular 90-Day Optimization</li><li><b>Unlimited 24/7 Tier 3 Technician Support</b></li><li>Online Identity Theft Protection</li></ul>
    <div class="more">LEARN MORE</div>
  </div>
</section>

<section class="why-join">
  <div class="emblem" style="top:22px"></div>
  <h2 class="section-title" style="top:96px">Why Join Us</h2>
  <div class="why-item" style="left:172px;top:166px"><h4>Best reviews in the entire industry</h4><p>Lorem Ipsum is simply dummy text of the printing and typesetting industry.</p></div>
  <div class="why-item" style="left:673px;top:166px"><h4>Exceptional Service &amp; Guarantee</h4><p>Lorem Ipsum is simply dummy text of the printing and typesetting industry.</p></div>
  <div class="why-item" style="left:172px;top:285px"><h4>Experience and Expert IT Technicians</h4><p>Lorem Ipsum is simply dummy text of the printing and typesetting industry.</p></div>
  <div class="why-item" style="left:673px;top:285px"><h4>Best Technology and Partners</h4><p>Lorem Ipsum is simply dummy text of the printing and typesetting industry.</p></div>
  <div class="devices" role="img" aria-label="Tablet, laptop, desktop monitor and phone shown side by side"></div>
</section>

<section class="features">
  <div class="emblem" style="top:10px"></div>
  <h2 class="section-title" style="top:84px">All the best features, at the best price!</h2>
  <p class="section-lead" style="top:134px">Lorem Ipsum is simply dummy text of the printing and typesetting industry. Lorem Ipsum has been the industry's standard dummy text ever since the 1500s</p>

  <div class="feature-item" style="left:185px;top:208px">
    <svg width="150" height="150" viewBox="0 0 150 150"><circle cx="75" cy="75" r="64" fill="none" stroke="var(--ring)" stroke-width="18"/><path d="M75 11a64 64 0 0164 64" fill="none" stroke="var(--blue)" stroke-width="18"/><rect x="52" y="58" width="46" height="30" rx="3" fill="#fff" stroke="#666" stroke-width="3"/><path d="M60 73h30" stroke="#666" stroke-width="3"/></svg>
    <h5>Ad Blocker</h5><p>Avoid unwanted Pop-ups with the newest Ad Blocking technology.</p>
  </div>
  <div class="feature-item" style="left:404px;top:208px">
    <svg width="150" height="150" viewBox="0 0 150 150"><circle cx="75" cy="75" r="64" fill="none" stroke="var(--ring)" stroke-width="18"/><path d="M75 11a64 64 0 0164 64" fill="none" stroke="var(--blue)" stroke-width="18"/><rect x="50" y="55" width="50" height="34" rx="3" fill="#fff" stroke="#666" stroke-width="3"/><path d="M56 84l12-14 9 8 8-6 9 12z" fill="#5bb05b"/></svg>
    <h5>Regular Tune-Ups</h5><p>Get a Regular Tune-Up and Optimization every 90 days.</p>
  </div>
  <div class="feature-item" style="left:623px;top:208px">
    <svg width="150" height="150" viewBox="0 0 150 150"><circle cx="75" cy="75" r="64" fill="none" stroke="var(--ring)" stroke-width="18"/><path d="M75 11a64 64 0 0156 33" fill="none" stroke="var(--blue)" stroke-width="18"/><rect x="55" y="52" width="40" height="46" rx="3" fill="#fff" stroke="#666" stroke-width="3"/><path d="M63 64h24M63 74h24M63 84h16" stroke="#5bb05b" stroke-width="3"/></svg>
    <h5>System Reports</h5><p>Stay up to date with Real-Time System Reporting.</p>
  </div>
  <div class="feature-item" style="left:842px;top:208px">
    <svg width="150" height="150" viewBox="0 0 150 150"><circle cx="75" cy="75" r="64" fill="none" stroke="var(--ring)" stroke-width="18"/><path d="M75 11a64 64 0 0164 64" fill="none" stroke="var(--blue)" stroke-width="18"/><rect x="52" y="54" width="26" height="20" fill="#fff" stroke="#666" stroke-width="3"/><rect x="76" y="78" width="24" height="18" fill="#fff" stroke="#666" stroke-width="3"/><path d="M65 74v14h11" stroke="#f5821f" stroke-width="3" fill="none"/></svg>
    <h5>Multiple Devices</h5><p>Get support for up to 4 multiple devices. Ask about our Family Plans.</p>
  </div>

  <div class="feature-item" style="left:185px;top:513px">
    <svg width="150" height="150" viewBox="0 0 150 150"><circle cx="75" cy="75" r="64" fill="none" stroke="var(--ring)" stroke-width="18"/><path d="M75 11a64 64 0 0164 64" fill="none" stroke="var(--blue)" stroke-width="18"/><rect x="52" y="55" width="46" height="34" rx="3" fill="#fff" stroke="#666" stroke-width="3"/><circle cx="75" cy="72" r="8" fill="#5bb05b"/></svg>
    <h5>Identity Protection</h5><p>Coming Soon.</p>
  </div>
  <div class="feature-item" style="left:404px;top:513px">
    <svg width="150" height="150" viewBox="0 0 150 150"><circle cx="75" cy="75" r="64" fill="none" stroke="var(--ring)" stroke-width="18"/><path d="M75 11a64 64 0 0156 33" fill="none" stroke="var(--blue)" stroke-width="18"/><rect x="62" y="48" width="26" height="52" rx="4" fill="#fff" stroke="#666" stroke-width="3"/><rect x="67" y="56" width="16" height="30" fill="#5bb05b"/></svg>
    <h5>Mobile Security</h5><p>Coming Soon.</p>
  </div>
  <div class="feature-item" style="left:623px;top:513px">
    <svg width="150" height="150" viewBox="0 0 150 150"><circle cx="75" cy="75" r="64" fill="none" stroke="var(--ring)" stroke-width="18"/><path d="M75 11a64 64 0 0164 64" fill="none" stroke="var(--blue)" stroke-width="18"/><rect x="50" y="52" width="38" height="28" fill="#fff" stroke="#666" stroke-width="3"/><rect x="78" y="68" width="20" height="32" rx="3" fill="#fff" stroke="#666" stroke-width="3"/><rect x="56" y="58" width="26" height="16" fill="#5bb05b"/></svg>
    <h5>Cross Platform</h5><p>One Support Plan for different types of devices.</p>
  </div>
  <div class="feature-item" style="left:842px;top:513px">
    <svg width="150" height="150" viewBox="0 0 150 150"><circle cx="75" cy="75" r="64" fill="none" stroke="var(--ring)" stroke-width="18"/><path d="M75 11a64 64 0 0164 64" fill="none" stroke="var(--blue)" stroke-width="18"/><path d="M60 88h-4a10 10 0 010-20 15 15 0 0128-4 10 10 0 014 24h-4" fill="#fff" stroke="#666" stroke-width="3"/><path d="M75 74v20M69 88l6 6 6-6" stroke="#666" stroke-width="3" fill="none"/></svg>
    <h5>Cloud Backup</h5><p>Keep your data safe! Ask about our plans for Unlimited Cloud Backup.</p>
  </div>
</section>

<section class="consult">
  <div class="skyline" role="img" aria-label="City skyline silhouette"></div>
  <div class="emblem" style="top:22px"></div>
  <h2 class="section-title" style="top:96px;line-height:50px">Get a 30-minute one-on-one free<br>consultation with one of our experts!</h2>
  <div class="video">
    <div class="video-inner" role="img" aria-label="Video still of a dim office hallway"></div>
    <svg width="86" height="86" viewBox="0 0 86 86"><circle cx="43" cy="43" r="40" fill="none" stroke="#fff" stroke-width="4"/><path d="M34 26l26 17-26 17z" fill="#fff"/></svg>
  </div>
</section>

<section class="request">
  <h2>REQUEST YOUR PERSONAL OFFER NOW!</h2>
  <div class="field" style="left:158px;top:103px">Name</div>
  <div class="field" style="left:457px;top:103px">Email</div>
  <div class="field" style="left:757px;top:103px">Telephone Number</div>
  <div class="field" style="left:158px;top:167px">City</div>
  <div class="field" style="left:457px;top:167px">State</div>
  <div class="field" style="left:757px;top:167px">Pin</div>
  <div class="btn help">Get Help Now!</div>
</section>

<footer class="site-footer">
  <div class="foot-brand"><span></span>brightdesk</div>
  <p class="foot-about">You can get in touch with us any time of the day, any day of the week. We offer support through phone and online chat.</p>
  <div class="follow">Follow Us: <i></i><i></i></div>
  <div class="call">CALL US : (888) 555-0142</div>

  <div class="plans-col foot-col"><h6>PLANS</h6><ul style="margin-top:8px"><li>Premium Plan</li><li>Premium Plus Plan</li><li>Platinum Plan</li></ul></div>
  <div class="mail">info@brightdesk.com</div>

  <div class="news-col foot-col"><h6>NEWSLETTER SIGNUP</h6><p>Sign up for our regular informational newsletters</p></div>
  <div class="email-input">e-mail</div>
  <div class="btn signup">SIGN UP</div>
  <div class="badge" style="left:770px;top:238px;width:90px;height:44px;border-radius:4px"></div>
  <div class="badge" style="left:870px;width:72px;border-radius:50% 50% 8px 8px;background:#c9302c"></div>
  <div class="badge" style="left:955px;width:70px;border-radius:50%;background:#d4a52a"></div>

  <div class="copyright">Brightdesk© 2016. All rights reserved. Terms and Conditions · Refund Policy · Privacy Policy</div>
</footer>

</body>
</html>
```